Sports medicine multidisciplinary brochures

Multi-disciplinary sports medicine clinic. Need a range of pamphlet / foldable brochures to advertise our various services. Looking at keeping a similar 'look' between the various brochures to still ID as being part of the group, but perhaps slight colour variation / different front pic to distinguish them. Looking at a pamphlet for: 1) General clinic (about us) info 2) Concussion info 3) Podiatry 4) Sports Physicians 5) Exercise Physiology 6) Osteoarthritis 7) Physiotherapy. Modern feel, but still warm / inviting. See attached logo / cards / etc. Thank you!

Target Market(s)

Athletes, sports injuries + general health / medical

Industry/Entity Type

Clinic

Requirements
Nice to have
• Simple, warm design. Activity / health / lifestyle related feel.
• Design to allow easy adaptation of wording / content.

```html
<!DOCTYPE html>
<html lang="en">
<head>
<meta charset="utf-8">
<title>Kora Sports and Joint Clinic – Brochure Cover</title>
<link href="https://fonts.googleapis.com/css2?family=Montserrat:wght@400;500;600;700&display=swap" rel="stylesheet">
<style>
  :root {
    --bg: #e6e6e6;
    --ink-black: #221f20;
    --band-orange: #e87022;
    --text-orange: #f07a22;
    --brand-green: #2a9b63;
    --white: #ffffff;
    --sky-deep: #7a1a08;
    --sky-mid: #d9461a;
    --sky-light: #f2792a;
  }
  * { box-sizing: border-box; margin: 0; padding: 0; }
  html, body {
    width: 1200px; height: 960px; overflow: hidden;
    background: var(--bg);
    font-family: "Montserrat", sans-serif;
  }
  .spread {
    position: absolute; left: 40px; top: 81px;
    width: 1120px; height: 798px;
    display: flex;
  }
  .panel { position: relative; width: 560px; height: 798px; overflow: hidden; }

  /* Back panel */
  .back .about {
    position: absolute; left: 0; top: 0; width: 560px; height: 602px;
    background: var(--ink-black);
  }
  .about-text {
    position: absolute; left: 59px; top: 402px; width: 442px;
    color: var(--text-orange); text-align: center;
    font-size: 10.6px; line-height: 14px; font-weight: 500;
    text-transform: uppercase;
  }
  .about-cta {
    position: absolute; left: 59px; top: 553px; width: 442px;
    color: var(--text-orange); text-align: center;
    font-size: 10.6px; font-weight: 700; text-transform: uppercase;
  }
  .back .info-band {
    position: absolute; left: 0; top: 602px; width: 560px; height: 196px;
    background: var(--band-orange); color: var(--white);
  }
  .info-heading {
    font-size: 10.5px; font-weight: 700; text-transform: uppercase;
    margin-bottom: 14px;
  }
  .hours { position: absolute; left: 31px; top: 29px; width: 231px; }
  .hours-table { width: 100%; border-collapse: collapse; font-size: 8.6px; }
  .hours-table td { padding: 3px 0 4px; border-top: 1px solid rgba(255,255,255,0.75); }
  .hours-table tr:first-child td { border-top: none; }
  .hours-table td:last-child { text-align: right; }
  .contact { position: absolute; left: 294px; top: 29px; width: 240px; font-size: 8.6px; line-height: 11px; }
  .contact p { margin-bottom: 11px; }

  /* Front panel */
  .front .hero {
    position: absolute; left: 0; top: 0; width: 560px; height: 445px;
    background:
      radial-gradient(ellipse at 50% 90%, var(--sky-light) 0%, transparent 60%),
      linear-gradient(180deg, var(--sky-mid) 0%, var(--sky-deep) 45%, var(--sky-mid) 75%, var(--sky-light) 100%);
  }
  .front .brand-band {
    position: absolute; left: 0; top: 445px; width: 560px; height: 157px;
    background: var(--ink-black);
  }
  .brand-name {
    position: absolute; left: 0; top: 500px; width: 560px;
    text-align: center; color: var(--brand-green);
    font-size: 42px; font-weight: 700; letter-spacing: 3px;
  }
  .front .tagline-band {
    position: absolute; left: 0; top: 602px; width: 560px; height: 196px;
    background: var(--band-orange);
  }
  .tagline {
    position: absolute; left: 60px; top: 60px; width: 440px;
    color: var(--white); text-align: center; text-transform: uppercase;
    font-size: 14.5px; line-height: 18.5px; font-weight: 600;
  }
</style>
</head>
<body>
  <main class="spread">
    <section class="panel back">
      <div class="about">
        <p class="about-text">The Kora Sports and Joint Clinic (KORA) is a new multidisciplinary clinic with specialist sports and exercise physicians as the leads. This is unique in Adelaide, aiming to provide affordable, evidence based, non-surgical treatment for sport and musculoskeletal injuries, as well as osteoarthritis. Combining specialist physician overview with select physiotherapists, podiatry, and other allied health integrated with use of our new fully equipped gym and modern software, Kora is uniquely positioned to work with you.</p>
        <p class="about-cta">For appointments, please call 08 7010 4426</p>
      </div>
      <div class="info-band">
        <div class="hours">
          <h2 class="info-heading">Opening Hours</h2>
          <table class="hours-table">
            <tr><td>Monday - Wednesday 8:30 - 6</td><td>8:30 - 6</td></tr>
            <tr><td>Thursday 8:30 - 8</td><td>8:30 - 8</td></tr>
            <tr><td>Friday 8:30 - 3</td><td>8:30 - 3</td></tr>
            <tr><td>Saturday 9 - 12:30</td><td>9 - 12:30</td></tr>
          </table>
        </div>
        <div class="contact">
          <h2 class="info-heading">Contact Details</h2>
          <p>Kora Sports and Joint Clinic<br>14 Harbour Row, Westbrook 5090</p>
          <p>Telephone 08 7010 4426</p>
          <p>hello@korajointclinic.com.au<br>www.korajointclinic.com.au</p>
        </div>
      </div>
    </section>

    <section class="panel front">
      <div class="hero" role="img" aria-label="Silhouettes of two athletes running against a fiery orange sunset sky"></div>
      <div class="brand-band"></div>
      <div class="brand-name">KORA</div>
      <div class="tagline-band">
        <p class="tagline">The Kora Sports and Joint Clinic (KORA) is a new multidisciplinary clinic with specialist sports and exercise physicians as the leads.</p>
      </div>
    </section>
  </main>
</body>
</html>
```